Marine Services Letterhead design

We need a letterhead design for an Australian owned company in Victoria named K+K Harbour Works Pty Ltd. We provide linesmen and launches to assist the large ships that come into port.
Our colour is orange.
The final design should have a strong nautical theme and communicate safety and reliability.
I would like to use the letter head on invoices so it should print to pdf well.

Target Market(s)

Owners and representatives of shipping companies. It is not for general public

Industry/Entity Type

Nautical

Requirements
Must have
• A shipping theme, not overly complicated, featuring safety orange colours but not all orange of course.
The letterhead should just sit at the top of the page so I can use for invoices.
Nice to have
• Something elegant and stylish
Should not have
• cartoons or pop art

```html
<!DOCTYPE html>
<html lang="en">
<head>
<meta charset="utf-8">
<title>K+K Harbour Works Pty Ltd – Letterhead</title>
<link href="https://fonts.googleapis.com/css2?family=Source+Sans+3:wght@400;600&display=swap" rel="stylesheet">
<style>
  :root {
    --paper: #ffffff;
    --ink: #1f1f1f;
    --rust: #b0692a;
    --sand: #ecdccd;
    --footer-text: #ffffff;
    --brand-mark: #d98a3c;
  }
  * { margin: 0; padding: 0; box-sizing: border-box; }
  html, body {
    width: 944px;
    height: 1200px;
    overflow: hidden;
    background: var(--paper);
  }
  .letterhead {
    position: relative;
    width: 944px;
    height: 1200px;
    background: var(--paper);
    font-family: "Source Sans 3", "Myriad Pro", sans-serif;
  }
  .brand {
    position: absolute;
    top: 52px;
    left: 0;
    width: 100%;
    display: flex;
    flex-direction: column;
    align-items: center;
    gap: 18px;
  }
  .brand-mark {
    width: 160px;
    height: 160px;
    border-radius: 50%;
    background: var(--brand-mark);
  }
  .brand-name {
    font-weight: 600;
    font-size: 22px;
    line-height: 1.1;
    color: var(--ink);
    letter-spacing: 0.1px;
  }
  .footer-art {
    position: absolute;
    left: 0;
    top: 0;
    width: 944px;
    height: 1200px;
  }
  .contact {
    position: absolute;
    top: 1160px;
    left: 0;
    width: 100%;
    display: flex;
    justify-content: center;
    align-items: center;
    gap: 24px;
    color: var(--footer-text);
    font-size: 18px;
    line-height: 1.2;
    font-weight: 400;
    padding-left: 6px;
  }
  .contact-item {
    display: flex;
    align-items: center;
    gap: 5px;
    white-space: nowrap;
  }
  .contact-abn { margin-left: 8px; }
  .contact-icon { width: 14px; height: 18px; fill: var(--footer-text); }
  .contact-icon--phone { width: 17px; }
</style>
</head>
<body>
<div class="letterhead">
  <header class="brand">
    <div class="brand-mark"></div>
    <div class="brand-name">K+K Harbour Works Pty Ltd</div>
  </header>

  <svg class="footer-art" viewBox="0 0 944 1200" aria-hidden="true">
    <path d="M0 1100 Q472 1170 944 1100 L944 1200 L0 1200 Z" fill="var(--rust)"/>
    <path d="M60 1088 Q472 1150 884 1088" fill="none" stroke="var(--sand)" stroke-width="6"/>
    <polygon points="40,1085 60.7,1097 63.3,1079" fill="var(--sand)"/>
    <polygon points="904,1085 883.3,1097 880.7,1079" fill="var(--sand)"/>
  </svg>

  <footer class="contact">
    <span class="contact-item">
      <svg class="contact-icon" viewBox="0 0 14 18"><path d="M7 0C3.1 0 0 3 0 6.8 0 11.5 7 18 7 18s7-6.5 7-11.2C14 3 10.9 0 7 0zm0 9.5A2.6 2.6 0 1 1 7 4.3a2.6 2.6 0 0 1 0 5.2z"/></svg>
      PO Box 214 Kilmore Bay 3981
    </span>
    <span class="contact-item">
      <svg class="contact-icon contact-icon--phone" viewBox="0 0 18 18"><circle cx="9" cy="9" r="8" fill="none" stroke="#fff" stroke-width="1.4"/><path d="M6.2 4.5l1.6 2.2-1 1.1c.6 1.3 1.5 2.2 2.8 2.9l1.1-1 2.2 1.6-.9 1.8c-3.7-.4-6.3-3-6.8-6.8z"/></svg>
      1300 647 218
    </span>
    <span class="contact-item contact-abn">ABN: 72396418855</span>
  </footer>
</div>
</body>
</html>
```